Business Cards and Stationery for a laboratory quality consulting business
Brennick Quality Solutions
Creative Brief
Simple
Marion Brennick
Principal Consultant
4817 Thistlewood Lane Cary, NC 27604
marion@brennickquality.example
www.brennickquality.example

```html
<!DOCTYPE html>
<html lang="en">
<head>
<meta charset="utf-8">
<title>Brennick Quality Solutions – Business Card</title>
<link href="https://fonts.googleapis.com/css2?family=Montserrat:wght@400;500;600;700&display=swap" rel="stylesheet">
<style>
  :root {
    --teal: #0c8a8c;
    --teal-dark: #17676c;
    --orange: #f4a81d;
    --white: #ffffff;
    --backdrop: #e9e9e9;
  }
  * { margin: 0; padding: 0; box-sizing: border-box; }
  html, body {
    width: 1200px;
    height: 818px;
    overflow: hidden;
    background: var(--backdrop);
    font-family: "Montserrat", Arial, sans-serif;
  }
  .business-card {
    position: absolute;
    left: 329px;
    top: 240px;
    width: 547px;
    height: 326px;
    background: var(--white);
    overflow: hidden;
    box-shadow: 0 8px 16px rgba(0,0,0,0.2);
  }
  .card-bands {
    position: absolute;
    left: 0;
    top: 0;
    width: 547px;
    height: 326px;
  }
  .brand {
    position: absolute;
    left: 48px;
    top: 140px;
    display: flex;
    align-items: center;
    gap: 10px;
  }
  .brand-dot {
    width: 30px;
    height: 30px;
    border-radius: 50%;
    background: var(--orange);
    flex: none;
  }
  .brand-name {
    color: var(--teal);
    font-weight: 700;
    font-size: 19px;
    line-height: 1.15;
    width: 180px;
  }
  .divider {
    position: absolute;
    left: 286px;
    top: 74px;
    width: 2px;
    height: 176px;
    background: var(--orange);
  }
  .contact {
    position: absolute;
    left: 298px;
    top: 0;
    color: var(--teal-dark);
  }
  .contact > div {
    position: absolute;
    left: 0;
    white-space: nowrap;
  }
  .contact-name {
    top: 86px;
    font-size: 18px;
    font-weight: 600;
    color: var(--teal);
  }
  .contact-title {
    top: 111px;
    font-size: 9px;
    font-weight: 500;
    color: var(--orange);
  }
  .contact-line {
    font-size: 12.5px;
    font-weight: 500;
  }
  .line-street { top: 131px; }
  .line-city   { top: 149px; }
  .line-cell   { top: 176px; }
  .line-email  { top: 203px; }
  .line-web    { top: 229px; }
</style>
</head>
<body>
  <div class="business-card">
    <svg class="card-bands" viewBox="0 0 547 326" aria-hidden="true">
      <path d="M0 0 H547 V40 Q273 8 0 40 Z" fill="var(--orange)"/>
      <path d="M0 0 H547 V32 Q273 0 0 32 Z" fill="var(--teal)"/>
      <path d="M0 286 Q273 318 547 286 V326 H0 Z" fill="var(--orange)"/>
      <path d="M0 294 Q273 326 547 294 V326 H0 Z" fill="var(--teal)"/>
    </svg>

    <div class="brand">
      <span class="brand-dot"></span>
      <span class="brand-name">Brennick Quality Solutions</span>
    </div>

    <div class="divider"></div>

    <div class="contact">
      <div class="contact-name">Marion Brennick</div>
      <div class="contact-title">Principal Consultant</div>
      <div class="contact-line line-street">4817 Thistlewood Lane</div>
      <div class="contact-line line-city">Cary, NC 27604</div>
      <div class="contact-line line-cell">Cell : 919-555-0148</div>
      <div class="contact-line line-email">marion@brennickquality.example</div>
      <div class="contact-line line-web">www.brennickquality.example</div>
    </div>
  </div>
</body>
</html>
```